Silverleaf Coverage Partners, LLC
Business cards, letterhead, envelopes, and mailing labels (3.43" x 1.93")
Silverleaf Coverage Partners, LLC - Medical
Creative Brief
Professional
Colin R. Thackery
Licensed Insurance Agent
Post Office Box 417 Destin, FL 32586
colin@silverleafcovers.example
Appointed with all major insurers - Northgate WellCare - OPWL Velora Broadfield WellnessCare Keystone of Tarrow and Lindon of Tarrow Vital Bridge Select Halvik Silverleaf Coverage Partners, LLC Helping find the best plan for your needs!

```html
<!DOCTYPE html>
<html lang="en">
<head>
<meta charset="utf-8">
<title>Silverleaf Coverage Partners, LLC – Business Card</title>
<link href="https://fonts.googleapis.com/css2?family=Tinos&family=Open+Sans:ital,wght@0,700;1,700&display=swap" rel="stylesheet">
<style>
  :root {
    --backdrop: #e4e5e7;
    --card: #ffffff;
    --brand-blue: #1d5fb0;
    --band-blue: #1f63c4;
    --brand-green: #37b83a;
    --text-grey: #4a4a4a;
    --divider: #c9c9c9;
    --icon: #3f6fa6;
  }
  html, body {
    margin: 0;
    width: 1200px;
    height: 780px;
    overflow: hidden;
    background: var(--backdrop);
  }
  .canvas {
    position: relative;
    width: 1200px;
    height: 780px;
  }
  .business-card {
    position: absolute;
    left: 40px;
    top: 70px;
    width: 1120px;
    height: 640px;
    background: var(--card);
    border-radius: 30px;
    overflow: hidden;
    box-shadow: 0 6px 22px rgba(0,0,0,0.18);
  }
  .brand {
    position: absolute;
    left: 105px;
    top: 95px;
    display: flex;
    align-items: center;
    gap: 22px;
  }
  .brand-square {
    width: 96px;
    height: 96px;
    background: var(--brand-green);
  }
  .brand-name {
    font-family: "Tinos", "Times New Roman", serif;
    font-size: 44px;
    color: var(--brand-blue);
    white-space: nowrap;
  }
  .agent {
    position: absolute;
    right: 730px;
    top: 300px;
    text-align: right;
  }
  .agent-name {
    font-family: "Open Sans", Arial, sans-serif;
    font-weight: 700;
    font-size: 34px;
    color: var(--brand-blue);
    margin: 0;
    line-height: 1.2;
  }
  .agent-title {
    font-family: "Open Sans", Arial, sans-serif;
    font-weight: 700;
    font-style: italic;
    font-size: 23px;
    color: var(--brand-green);
    margin: 2px 0 22px;
  }
  .agent-address {
    font-family: "Tinos", "Times New Roman", serif;
    font-size: 25px;
    color: var(--text-grey);
    line-height: 1.25;
    font-style: normal;
  }
  .divider {
    position: absolute;
    left: 420px;
    top: 300px;
    width: 2px;
    height: 215px;
    background: var(--divider);
  }
  .contact-list {
    position: absolute;
    left: 450px;
    top: 298px;
    margin: 0;
    padding: 0;
    list-style: none;
    font-family: "Tinos", "Times New Roman", serif;
    font-size: 25px;
    color: var(--text-grey);
  }
  .contact-list li {
    display: flex;
    align-items: center;
    gap: 14px;
    height: 43px;
  }
  .contact-icon {
    width: 24px;
    height: 24px;
    flex: none;
  }
  .wave {
    position: absolute;
    left: 0;
    bottom: 0;
    width: 1120px;
    height: 200px;
  }
</style>
</head>
<body>
<div class="canvas">
  <div class="business-card">
    <div class="brand">
      <div class="brand-square"></div>
      <div class="brand-name">Silverleaf Coverage Partners, LLC</div>
    </div>

    <div class="agent">
      <p class="agent-name">Colin R. Thackery</p>
      <p class="agent-title">Licensed Insurance Agent</p>
      <address class="agent-address">Post Office Box 417<br>Destin, FL 32586</address>
    </div>

    <div class="divider"></div>

    <ul class="contact-list">
      <li>
        <svg class="contact-icon" viewBox="0 0 24 24" aria-hidden="true"><path fill="var(--icon)" d="M6.6 10.8a15 15 0 0 0 6.6 6.6l2.2-2.2a1 1 0 0 1 1-.25 11.4 11.4 0 0 0 3.6.57 1 1 0 0 1 1 1V20a1 1 0 0 1-1 1A17 17 0 0 1 3 4a1 1 0 0 1 1-1h3.5a1 1 0 0 1 1 1c0 1.25.2 2.45.57 3.6a1 1 0 0 1-.25 1z"/></svg>
        <span>8885550147 (T)</span>
      </li>
      <li>
        <svg class="contact-icon" viewBox="0 0 24 24" aria-hidden="true"><rect x="6" y="2" width="12" height="20" rx="2" fill="var(--icon)"/><rect x="8" y="5" width="8" height="11" fill="#fff"/><circle cx="12" cy="19" r="1.2" fill="#fff"/></svg>
        <span>8505550162</span>
      </li>
      <li>
        <svg class="contact-icon" viewBox="0 0 24 24" aria-hidden="true"><rect x="3" y="9" width="18" height="12" rx="2" fill="var(--icon)"/><rect x="7" y="3" width="10" height="7" fill="var(--icon)"/><rect x="8" y="4" width="8" height="5" fill="#fff"/><rect x="6" y="13" width="12" height="2" fill="#fff"/></svg>
        <span>8775550193</span>
      </li>
      <li>
        <svg class="contact-icon" viewBox="0 0 24 24" aria-hidden="true"><circle cx="12" cy="12" r="4" fill="none" stroke="var(--icon)" stroke-width="2.4"/><path d="M16 8v5.5a2.5 2.5 0 0 0 5 0V12a9 9 0 1 0-3.5 7.1" fill="none" stroke="var(--icon)" stroke-width="2.4"/></svg>
        <span>colin@silverleafcovers.example</span>
      </li>
      <li>
        <svg class="contact-icon" viewBox="0 0 24 24" aria-hidden="true"><circle cx="12" cy="12" r="9" fill="none" stroke="var(--icon)" stroke-width="2"/><ellipse cx="12" cy="12" rx="4" ry="9" fill="none" stroke="var(--icon)" stroke-width="1.6"/><line x1="3" y1="12" x2="21" y2="12" stroke="var(--icon)" stroke-width="1.6"/></svg>
        <span>silverleafcovers.example</span>
      </li>
    </ul>

    <svg class="wave" viewBox="0 0 1120 200" preserveAspectRatio="none" aria-hidden="true">
      <path d="M0 40 C 320 110 720 140 1120 128 L1120 138 C 720 152 320 130 0 62 Z" fill="var(--brand-green)"/>
      <path d="M0 78 C 320 145 720 165 1120 152 L1120 200 L0 200 Z" fill="var(--band-blue)"/>
    </svg>
  </div>
</div>
</body>
</html>
```